Creative & Appealing Business Card

Required a business card for Vantrelink
We specialise in claims management services for PPI ( Payment Protection Insurance.
2 sided business card
Round Corners
I like embossed and raised lettering

```html
<!DOCTYPE html>
<html lang="en">
<head>
<meta charset="utf-8">
<title>Vantrelink Business Card</title>
<link rel="stylesheet" href="https://fonts.googleapis.com/css2?family=Jost:wght@400;500;600&display=swap">
<style>
  :root {
    --page-bg: #e9e9e9;
    --card-bg: #ffffff;
    --band: #3f5761;
    --band-text: #ffffff;
    --ink: #3d3d3d;
    --ink-soft: #4c4c4c;
    --rule: #3f5761;
    --faint-mark: #ececec;
  }
  * { box-sizing: border-box; }
  html, body {
    margin: 0;
    width: 1025px;
    height: 1200px;
    overflow: hidden;
    background: var(--page-bg);
    font-family: "Jost", sans-serif;
    color: var(--ink);
  }
  .card {
    position: absolute;
    left: 50px;
    width: 925px;
    height: 520px;
    background: var(--card-bg);
    overflow: hidden;
    box-shadow: 0 2px 6px rgba(0,0,0,0.12);
  }
  .card--front { top: 55px; }
  .card--back { top: 625px; }

  .card__header {
    position: absolute;
    top: 18px; left: 0; right: 0;
    height: 112px;
    background: var(--band);
    display: flex;
    align-items: center;
    justify-content: center;
    gap: 16px;
  }
  .brand-dot {
    width: 54px; height: 54px;
    border-radius: 50%;
    background: var(--band-text);
  }
  .brand-name {
    font-size: 34px;
    font-weight: 600;
    color: var(--band-text);
    letter-spacing: 0.2px;
  }
  .card__footer {
    position: absolute;
    bottom: 0; left: 0; right: 0;
    height: 16px;
    background: var(--band);
  }
  .faint-mark {
    position: absolute;
    right: 40px;
    width: 190px; height: 190px;
    border-radius: 50%;
    background: var(--faint-mark);
  }
  .card--front .faint-mark { top: 290px; }
  .card--back .faint-mark { top: 280px; }

  /* Front */
  .services {
    position: absolute;
    left: 12px;
    top: 330px;
  }
  .services__title {
    margin: 0;
    font-size: 24px;
    font-weight: 500;
    color: var(--ink);
  }
  .services__rule {
    width: 248px;
    height: 4px;
    background: var(--rule);
    margin: 4px 0 24px 0;
  }
  .services__list {
    list-style: none;
    margin: 0; padding: 0;
  }
  .services__list li {
    display: flex;
    align-items: center;
    gap: 10px;
    font-size: 22px;
    color: var(--ink-soft);
    margin-bottom: 10px;
  }
  .bullet {
    width: 15px; height: 15px;
    border-radius: 50%;
    background: var(--ink);
    margin-left: 2px;
  }

  /* Back */
  .person {
    position: absolute;
    right: 32px;
    top: 145px;
    text-align: right;
  }
  .person__name {
    margin: 0;
    font-size: 31px;
    font-weight: 400;
    letter-spacing: 0.5px;
    color: var(--ink);
    line-height: 1.1;
  }
  .person__rule {
    width: 245px;
    height: 5px;
    background: var(--rule);
    margin: 2px 0 6px auto;
  }
  .person__company {
    font-size: 22px;
    color: var(--ink-soft);
  }
  .contact {
    position: absolute;
    left: 28px;
    top: 310px;
    list-style: none;
    margin: 0; padding: 0;
  }
  .contact li {
    display: flex;
    align-items: center;
    gap: 6px;
    height: 35px;
    font-size: 21px;
    color: var(--ink-soft);
  }
  .contact svg {
    width: 22px; height: 22px;
    flex: none;
    fill: none;
    stroke: var(--ink);
    stroke-width: 2;
  }
  .contact .at-sign {
    width: 22px;
    text-align: center;
    font-size: 22px;
    font-weight: 500;
    color: var(--ink);
  }
</style>
</head>
<body>

<section class="card card--front" aria-label="Card front">
  <header class="card__header">
    <span class="brand-dot"></span>
    <span class="brand-name">Vantrelink</span>
  </header>
  <div class="faint-mark"></div>
  <div class="services">
    <h2 class="services__title">Claims Management Service for mis-sold:</h2>
    <div class="services__rule"></div>
    <ul class="services__list">
      <li><span class="bullet"></span>Payment Protection Insurance Claims</li>
      <li><span class="bullet"></span>Interest Rate Hedging Products / SWAPS</li>
    </ul>
  </div>
  <div class="card__footer"></div>
</section>

<section class="card card--back" aria-label="Card back">
  <header class="card__header">
    <span class="brand-dot"></span>
    <span class="brand-name">Vantrelink</span>
  </header>
  <div class="person">
    <h1 class="person__name">TARIQ MALDEN</h1>
    <div class="person__rule"></div>
    <div class="person__company">Vantrelink</div>
  </div>
  <div class="faint-mark"></div>
  <ul class="contact">
    <li>
      <svg viewBox="0 0 24 24" aria-hidden="true"><path d="M12 22s7-7 7-12a7 7 0 0 0-14 0c0 5 7 12 7 12z"/><circle cx="12" cy="10" r="2.5"/></svg>
      48 Ashvale Road London W7 2QN
    </li>
    <li>
      <svg viewBox="0 0 24 24" aria-hidden="true"><rect x="3" y="6" width="18" height="12"/><path d="M3 6l9 7 9-7"/></svg>
      tariq@vantrelink.com
    </li>
    <li>
      <svg viewBox="0 0 24 24" aria-hidden="true"><rect x="7" y="2" width="10" height="20" rx="1.5"/><path d="M10 18h4"/></svg>
      +44 (0) 333 000 0148
    </li>
    <li>
      <svg viewBox="0 0 24 24" aria-hidden="true"><rect x="7" y="3" width="10" height="6"/><rect x="3" y="9" width="18" height="8" fill="#3d3d3d"/><rect x="7" y="15" width="10" height="6"/></svg>
      +44 (0) 203 000 0562
    </li>
    <li>
      <span class="at-sign">@</span>
      www.vantrelink.com
    </li>
  </ul>
  <div class="card__footer"></div>
</section>

</body>
</html>
```